Quelvane FZE
Engineered for Silence
Quelvane FZE -
Creative Brief
Use specific fonts
Use your own creativity
Professional
T. Orlov
Managing Director & Chief Acoustic Consultant
P.O. Box - 58914, Calder Bay Free Zone
info@quelvane-example.com
www.quelvane-example.com
Please provide Business card, letter head, quotation, invoice, fax & envelop designs
Services & Products: Acoustic Consultants, Acoustic Contracting, Acoustic Spray, Acoustic Underlay, Load Bearing Pads, Acoustic Louvers, Sound Attenuators, Inertia Bases, Floating Floors, Acoustic Doors, Acoustic Barriers, Acoustic Enclosure, Generator Enclosure, Sand Trap Louvers, Extract Louvers, MEP Contracting

```html
<!DOCTYPE html>
<html lang="en">
<head>
<meta charset="utf-8">
<title>Quelvane FZE – Letterhead Set</title>
<link rel="stylesheet" href="https://fonts.googleapis.com/css2?family=Open+Sans:wght@400;600;700&display=swap">
<style>
  :root {
    --canvas: #ffffff;
    --paper: #ffffff;
    --paper-edge: #e3e3e3;
    --brand-blue: #1f5fa8;
    --brand-green: #5aa33a;
    --map-tone: #efefef;
    --map-fade: rgba(239,239,239,0);
    --footer-text: #8a8a8a;
    --page-number: #9a9a9a;
    --tint-top: #f6f6f6;
    --tint-bottom: #dcdcdc;
  }
  * { box-sizing: border-box; margin: 0; padding: 0; }
  html, body {
    width: 1200px; height: 593px; overflow: hidden;
    background: var(--canvas);
    font-family: "Open Sans", Arial, sans-serif;
  }
  .sheet-set { position: relative; width: 1200px; height: 593px; }
  .letterhead {
    position: absolute; top: 24px; width: 372px; height: 536px;
    background: var(--paper);
    border: 1px solid var(--paper-edge);
    box-shadow: 0 14px 12px -10px rgba(0,0,0,0.35);
    overflow: visible;
  }
  .letterhead--one { left: 14px; }
  .letterhead--two { left: 410px; }
  .letterhead--three {
    left: 806px;
    background: linear-gradient(180deg, var(--tint-top) 0%, #ffffff 35%, #f0f0f0 70%, var(--tint-bottom) 100%);
  }
  .page-number {
    position: absolute; top: -20px; left: 0; width: 100%;
    text-align: center; font-size: 9px; color: var(--page-number);
  }
  .world-map {
    position: absolute; top: 14px; left: 150px; width: 212px; height: 250px;
    background: radial-gradient(ellipse at 55% 42%, var(--map-tone) 0%, var(--map-tone) 30%, var(--map-fade) 70%);
  }
  .brand {
    position: absolute; top: 20px; left: 24px;
    display: flex; flex-direction: column; align-items: flex-start;
  }
  .brand-mark {
    width: 30px; height: 30px; border-radius: 50%;
    background: var(--brand-blue); margin-left: 22px; margin-bottom: 3px;
  }
  .brand-name {
    font-size: 15px; font-weight: 700; color: var(--brand-blue);
    letter-spacing: -0.2px; line-height: 18px;
  }
  .brand-tagline {
    font-size: 5px; font-weight: 600; color: var(--brand-green);
    letter-spacing: 0.6px; text-transform: uppercase; margin-top: 1px;
  }
  .contact-block {
    position: absolute; bottom: 14px; right: 22px; width: 150px;
    border-left: 2px solid var(--paper-edge); padding-left: 6px;
    font-size: 5.5px; line-height: 9px; color: var(--footer-text);
    font-style: normal; white-space: nowrap;
  }
  .letterhead--two .contact-block { border-left-color: var(--brand-blue); }
  .letterhead--three .contact-block { border-left-color: var(--brand-green); }
</style>
</head>
<body>
<main class="sheet-set">
  <section class="letterhead letterhead--one">
    <span class="page-number">1</span>
    <div class="world-map" role="img" aria-label="Faint world map showing Africa and Europe"></div>
    <div class="brand">
      <span class="brand-mark"></span>
      <span class="brand-name">QuelvaneFZE</span>
      <span class="brand-tagline">Engineered for Silence</span>
    </div>
    <address class="contact-block">
      P.O. Box - 58914, Calder Bay Free Zone<br>
      info@quelvane-example.com<br>
      www.quelvane-example.com
    </address>
  </section>

  <section class="letterhead letterhead--two">
    <span class="page-number">2</span>
    <div class="world-map" role="img" aria-label="Faint world map showing Africa and Europe"></div>
    <div class="brand">
      <span class="brand-mark"></span>
      <span class="brand-name">QuelvaneFZE</span>
      <span class="brand-tagline">Engineered for Silence</span>
    </div>
    <address class="contact-block">
      P.O. Box - 58914, Calder Bay Free Zone<br>
      info@quelvane-example.com<br>
      www.quelvane-example.com
    </address>
  </section>

  <section class="letterhead letterhead--three">
    <span class="page-number">3</span>
    <div class="world-map" role="img" aria-label="Faint world map showing Africa and Europe"></div>
    <div class="brand">
      <span class="brand-mark"></span>
      <span class="brand-name">QuelvaneFZE</span>
      <span class="brand-tagline">Engineered for Silence</span>
    </div>
    <address class="contact-block">
      P.O. Box - 58914, Calder Bay Free Zone<br>
      info@quelvane-example.com<br>
      www.quelvane-example.com
    </address>
  </section>
</main>
</body>
</html>
```